Small, static, 2 page website that promotes 3-6 workshops

This is a microsite for my company that promotes 3 (and later 6) security workshops for developers. The address is going to be codewacht-cursussen.nl so it is very important that the title reads 'Codewacht Cursussen' and the subtitle reads 'voor ontwikkelaars' (means for developers in dutch).

On the frontpage, there will be a small introduction text (about 50 words) about the workshops in general and there should be 3 workshops listed on the frontpage with also a small introduction text. All the workshops are cyber security/hacking related so maybe a small graphic for every workshop would lighten things up.

Then when a visitor clicks a 'more info' button a detail page about that specific workshop with a longer description, a date/location, a 'book now' button and a price should be show.

I have include a quick drawing of what I have in mind for the frontpage, this is not set in stone so you could come up with something else.

I also included my company logo, it should be clear on the site that these workshops are 'Halvard Shield' workshops.

Target Market(s)

Development companies looking for security workshops, the responsible people for those type of workshops are usually security officers, lead developers/managers or developers themselves.

Industry/Entity Type

It Company

Number of Pages Required

2 page

Font styles to use
Sans Serif
Other font styles liked:

Requirements
Must have
• 3 highlighted trainings on the frontpage and a detail page and the title and subtitle as headings on the page.
Nice to have
• I'd really like to have the 3 boxes on the frontpage to have icons or some sort of images. The first 3 workshops that are going to be on the page are:
• - Security awareness for developers
• - Web application security from a hackers perspective
• - Penetrationtesting for developers

```html
<!DOCTYPE html>
<html lang="nl">
<head>
<meta charset="utf-8">
<title>Codewacht Cursussen – voor ontwikkelaars</title>
<link rel="stylesheet" href="https://fonts.googleapis.com/css2?family=Roboto+Condensed:wght@300;400;700&display=swap">
<style>
  :root {
    --navy: #17406b;
    --navy-deep: #143a63;
    --circle-fill: #f2f2f2;
    --text-grey: #5f5f5f;
    --white: #ffffff;
    --logo-bg: rgba(236, 238, 241, 0.95);
    --hero-a: #6f8199;
    --hero-b: #a3b3c6;
    --hero-c: #8a9cb3;
  }
  * { box-sizing: border-box; margin: 0; padding: 0; }
  html, body { width: 1200px; height: 902px; overflow: hidden; background: var(--white); }
  body { position: relative; font-family: "Roboto Condensed", "Arial Narrow", sans-serif; }

  .hero {
    position: absolute; left: 0; top: 0; width: 1200px; height: 515px;
    background:
      radial-gradient(ellipse 420px 300px at 520px 260px, rgba(190,202,216,0.55), transparent 70%),
      linear-gradient(90deg, var(--hero-a) 0%, var(--hero-b) 48%, var(--hero-c) 100%);
  }

  .brand {
    position: absolute; left: 461px; top: 0; width: 279px; height: 91px;
    background: var(--logo-bg); border-radius: 0 0 4px 4px;
    display: flex; align-items: center; justify-content: center; gap: 12px;
  }
  .brand-dot { width: 26px; height: 26px; border-radius: 50%; background: var(--navy); }
  .brand-name { font-size: 27px; font-weight: 700; color: var(--navy); letter-spacing: 0.5px; }

  .site-title {
    position: absolute; left: 0; width: 1200px; top: 170px; text-align: center;
    font-size: 32px; font-weight: 700; color: var(--white); letter-spacing: 0.2px;
    text-shadow: 0 1px 3px rgba(0,0,0,0.25);
  }
  .site-subtitle {
    position: absolute; left: 0; width: 1200px; top: 207px; text-align: center;
    font-size: 14.5px; font-weight: 400; color: var(--white); text-transform: uppercase;
  }
  .intro {
    position: absolute; left: 326px; width: 548px; top: 283px; text-align: center;
    font-size: 14.5px; line-height: 21.7px; color: var(--white); font-weight: 400;
  }

  .workshop { position: absolute; top: 423px; width: 300px; text-align: center; }
  .workshop-1 { left: 148px; }
  .workshop-2 { left: 449px; }
  .workshop-3 { left: 751px; }

  .badge {
    width: 174px; height: 174px; margin: 0 auto; border-radius: 50%;
    border: 7px solid var(--navy); background: var(--circle-fill);
    display: flex; align-items: center; justify-content: center;
  }
  .connector { width: 2px; height: 30px; margin: 0 auto; border-left: 2px dashed var(--navy); }
  .connector-dot { width: 13px; height: 13px; margin: 0 auto; border-radius: 50%; background: var(--navy); }

  .workshop-title {
    margin-top: 16px; font-size: 12.3px; font-weight: 700; color: var(--navy);
    text-transform: uppercase; letter-spacing: 0.2px;
  }
  .workshop-text {
    margin: 15px auto 0; width: 256px; font-size: 10.6px; line-height: 12.6px;
    color: var(--text-grey); font-weight: 400;
  }
  .read-more {
    display: inline-block; margin-top: 15px; width: 86px; height: 31px; line-height: 31px;
    background: var(--navy); color: var(--white); border-radius: 4px;
    font-size: 11px; text-decoration: none;
  }

  .site-footer {
    position: absolute; left: 0; top: 850px; width: 1200px; height: 52px;
    background: var(--navy-deep); color: var(--white);
    font-size: 11px; text-align: center; line-height: 52px;
  }
</style>
</head>
<body>
  <div class="hero" role="img" aria-label="Blue-toned photo of a developer touching a digital interface with lines of code"></div>

  <header class="brand">
    <span class="brand-dot"></span>
    <span class="brand-name">Halvard Shield</span>
  </header>

  <h1 class="site-title">CODEWACHT CURSUSSEN</h1>
  <p class="site-subtitle">voor ontwikkelaars</p>

  <p class="intro">Lorem ipsum dolor sit amet, consectetur adipiscing elit. Fusce vitae arcu eros. Sed viverra sem a hendrerit dictum. Aenean eget bibendum est. Vestibulum euismod hendrerit nulla quis viverra. Vestibulum sodales egestas leo, at tristique dolor rhoncus id. Quisque et sem pretium, tincidunt ante id, tempor nulla. Morbi non ultricies turpis.</p>

  <section class="workshop workshop-1">
    <div class="badge">
      <svg width="72" height="82" viewBox="0 0 72 82" aria-hidden="true">
        <path d="M36 4 L66 14 V40 C66 60 52 72 36 78 C20 72 6 60 6 40 V14 Z" fill="none" stroke="#17406b" stroke-width="6" stroke-linejoin="round"/>
        <path d="M27 30 L18 40 L27 50 M45 30 L54 40 L45 50 M39 27 L33 53" fill="none" stroke="#17406b" stroke-width="3.5" stroke-linecap="round" stroke-linejoin="round"/>
      </svg>
    </div>
    <div class="connector"></div>
    <div class="connector-dot"></div>
    <h2 class="workshop-title">Security awareness for developers</h2>
    <p class="workshop-text">Lorem ipsum dolor sit amet, consectetur adipiscing elit. Fusce vitae arcu eros. Sed viverra sem a hendrerit dictum.</p>
    <a class="read-more" href="#">Read More</a>
  </section>

  <section class="workshop workshop-2">
    <div class="badge">
      <svg width="72" height="82" viewBox="0 0 72 82" aria-hidden="true">
        <path d="M36 4 L66 14 V40 C66 60 52 72 36 78 C20 72 6 60 6 40 V14 Z" fill="#17406b" stroke="#17406b" stroke-width="6" stroke-linejoin="round"/>
        <path d="M36 10 L60 18 V40 C60 56 49 66 36 71 C23 66 12 56 12 40 V18 Z" fill="#f2f2f2"/>
        <circle cx="36" cy="40" r="18" fill="#17406b"/>
        <path d="M28 30 C32 28 36 31 34 35 C32 38 27 37 26 41 C25 44 28 47 30 50 M42 26 C44 30 40 33 43 36 C46 39 50 37 52 40 M40 46 C43 47 44 51 42 55" fill="none" stroke="#f2f2f2" stroke-width="3" stroke-linecap="round"/>
      </svg>
    </div>
    <div class="connector"></div>
    <div class="connector-dot"></div>
    <h2 class="workshop-title">Web application security</h2>
    <p class="workshop-text">Lorem ipsum dolor sit amet, consectetur adipiscing elit. Fusce vitae arcu eros. Sed viverra sem a hendrerit dictum.</p>
    <a class="read-more" href="#">Read More</a>
  </section>

  <section class="workshop workshop-3">
    <div class="badge">
      <svg width="72" height="82" viewBox="0 0 72 82" aria-hidden="true">
        <path d="M36 4 L66 14 V40 C66 60 52 72 36 78 C20 72 6 60 6 40 V14 Z" fill="none" stroke="#17406b" stroke-width="6" stroke-linejoin="round"/>
        <rect x="22" y="36" width="28" height="22" rx="3" fill="#17406b"/>
        <path d="M28 36 V30 C28 24 33 21 37 22 C42 23 45 27 44 32" fill="none" stroke="#17406b" stroke-width="4.5" stroke-linecap="round"/>
        <circle cx="32" cy="47" r="5" fill="#f2f2f2"/>
        <circle cx="32" cy="47" r="2.2" fill="#17406b"/>
      </svg>
    </div>
    <div class="connector"></div>
    <div class="connector-dot"></div>
    <h2 class="workshop-title">Penetrationtesting for developers</h2>
    <p class="workshop-text">Lorem ipsum dolor sit amet, consectetur adipiscing elit. Fusce vitae arcu eros. Sed viverra sem a hendrerit dictum.</p>
    <a class="read-more" href="#">Read More</a>
  </section>

  <footer class="site-footer">© 2016 Halvard Shield. Al Right Reserved.</footer>
</body>
</html>
```